its a new company based in Christchurch new Zealand building computers ,repairs, upgrades and anything computers for the general public,i like bright happy colours like yellows, greens reds anything that stands out and it needs to communicant trust and security towards my new company,i have no logo yet,

Target Market(s)

target market of all ages

Industry/Entity Type

Building

Contact Information for Business Card

Pixel Harbour Limited,ph-0274829315,email-brightnode47@mailvista.example,14c tamworth cl,kelvale

```html
<!DOCTYPE html>
<html lang="en">
<head>
<meta charset="UTF-8">
<title>Pixel Harbour Limited – Business Cards</title>
<link rel="stylesheet" href="https://fonts.googleapis.com/css2?family=Orbitron:wght@900&family=Ubuntu:wght@400;500&display=swap">
<style>
  :root {
    --canvas-bg: #e9e6e1;
    --card-dark: #231f20;
    --text-light: #ffffff;
    --orange-a: #f7a234;
    --orange-b: #f58a1f;
    --orange-top: #fbd56a;
    --green-a: #b4d335;
    --green-b: #a5c82c;
    --screen-a: #5d8fd6;
    --screen-b: #2f5fa8;
    --frame: #2d2f3a;
  }
  * { margin: 0; padding: 0; box-sizing: border-box; }
  html, body {
    width: 1200px; height: 1000px; overflow: hidden;
    background: var(--canvas-bg);
    font-family: "Ubuntu", Arial, sans-serif;
  }
  .card {
    position: absolute; left: 215px;
    width: 770px; height: 440px;
    border-radius: 28px; overflow: hidden;
    box-shadow: 0 10px 28px rgba(0,0,0,.22);
  }
  .card--orange { top: 40px; --bullet: var(--orange-b); }
  .card--green  { top: 520px; --bullet: var(--green-a); }
  .card__bg { position: absolute; inset: 0; }
  .brand {
    position: absolute; left: 26px; top: 60px;
    color: var(--text-light); white-space: nowrap;
    font-family: "Ubuntu", Arial, sans-serif; font-weight: 500;
    font-size: 24px;
  }
  .holder-name {
    position: absolute; right: 30px; top: 18px;
    font-weight: 500; font-size: 22px;
    color: var(--text-light); letter-spacing: .5px;
  }
  .monitor {
    position: absolute; border-radius: 6px;
    background: linear-gradient(135deg, var(--screen-a), var(--screen-b));
    border: 8px solid var(--frame);
  }
  .monitor--diagnose { left: 150px; top: 118px; width: 150px; height: 110px; }
  .monitor--repair   { left: 325px; top: 88px;  width: 140px; height: 100px; }
  .monitor--blank    { left: 490px; top: 66px;  width: 130px; height: 92px; }
  .services {
    position: absolute; left: 548px; top: 180px; color: var(--text-light);
  }
  .services__title {
    font-family: "Orbitron", Arial, sans-serif; font-weight: 900;
    font-size: 19px; letter-spacing: 1px; text-transform: uppercase;
    margin-bottom: 4px;
  }
  .services__list { list-style: none; font-size: 16px; line-height: 24px; white-space: nowrap; }
  .services__list li::before {
    content: ""; display: inline-block; width: 9px; height: 9px;
    border-radius: 50%; background: var(--bullet); margin-right: 8px;
  }
  .contact { position: absolute; left: 26px; top: 268px; list-style: none; }
  .contact__item {
    display: flex; align-items: center; height: 40px;
    color: var(--text-light); font-size: 25px; white-space: nowrap;
  }
  .contact__icon { width: 32px; height: 32px; margin-right: 22px; flex: none; }
</style>
</head>
<body>

<section class="card card--orange">
  <svg class="card__bg" viewBox="0 0 770 440" aria-hidden="true">
    <defs>
      <linearGradient id="orange-fill" x1="0" y1="0" x2="1" y2="1">
        <stop offset="0" stop-color="var(--orange-top)"/>
        <stop offset=".35" stop-color="var(--orange-a)"/>
        <stop offset="1" stop-color="var(--orange-b)"/>
      </linearGradient>
    </defs>
    <rect width="770" height="440" fill="url(#orange-fill)"/>
    <path d="M0 22 H430 Q445 22 450 35 L455 48 Q460 58 475 58 H770 V380 H545 Q525 380 525 360 V270 Q525 250 505 250 H0 Z" fill="var(--card-dark)"/>
  </svg>
  <div class="brand">Pixel Harbour Limited</div>
  <div class="holder-name">YOUR NAME HERE</div>
  <div class="monitor monitor--diagnose" role="img" aria-label="Illustration of a computer monitor with a stethoscope for diagnostics"></div>
  <div class="monitor monitor--repair" role="img" aria-label="Illustration of a computer monitor with a screwdriver and wrench for repairs"></div>
  <div class="monitor monitor--blank" role="img" aria-label="Illustration of a computer monitor with keyboard"></div>
  <div class="services">
    <h2 class="services__title">Services</h2>
    <ul class="services__list">
      <li>Computer building</li>
      <li>Repairs, upgrades</li>
      <li>And anything of computers</li>
    </ul>
  </div>
  <ul class="contact">
    <li class="contact__item">
      <svg class="contact__icon" viewBox="0 0 32 32" aria-hidden="true"><circle cx="16" cy="16" r="15" fill="#fff"/><rect x="11" y="7" width="10" height="18" rx="2" fill="none" stroke="var(--orange-b)" stroke-width="2"/><rect x="13" y="10" width="6" height="6" fill="var(--orange-b)"/></svg>
      0274829315
    </li>
    <li class="contact__item">
      <svg class="contact__icon" viewBox="0 0 32 32" aria-hidden="true"><circle cx="16" cy="16" r="15" fill="#fff"/><rect x="8" y="10" width="16" height="12" rx="1" fill="var(--orange-b)"/><path d="M8 10 L16 17 L24 10" fill="none" stroke="#fff" stroke-width="1.5"/></svg>
      brightnode47@mailvista.example
    </li>
    <li class="contact__item">
      <svg class="contact__icon" viewBox="0 0 32 32" aria-hidden="true"><circle cx="16" cy="16" r="15" fill="#fff"/><path d="M16 25 C11 19 10 16 10 14 A6 6 0 0 1 22 14 C22 16 21 19 16 25 Z" fill="var(--orange-b)"/><circle cx="16" cy="14" r="2.2" fill="#fff"/></svg>
      14c tamworth cl,kelvale
    </li>
  </ul>
</section>

<section class="card card--green">
  <svg class="card__bg" viewBox="0 0 770 440" aria-hidden="true">
    <rect width="770" height="440" fill="var(--green-a)"/>
    <path d="M0 22 H430 Q445 22 450 35 L455 48 Q460 58 475 58 H770 V380 H545 Q525 380 525 360 V270 Q525 250 505 250 H0 Z" fill="var(--card-dark)"/>
  </svg>
  <div class="brand">Pixel Harbour Limited</div>
  <div class="holder-name">YOUR NAME HERE</div>
  <div class="monitor monitor--diagnose" role="img" aria-label="Illustration of a computer monitor with a stethoscope for diagnostics"></div>
  <div class="monitor monitor--repair" role="img" aria-label="Illustration of a computer monitor with a screwdriver and wrench for repairs"></div>
  <div class="monitor monitor--blank" role="img" aria-label="Illustration of a computer monitor with keyboard"></div>
  <div class="services">
    <h2 class="services__title">Services</h2>
    <ul class="services__list">
      <li>Computer building</li>
      <li>Repairs, upgrades</li>
      <li>And anything of computers</li>
    </ul>
  </div>
  <ul class="contact">
    <li class="contact__item">
      <svg class="contact__icon" viewBox="0 0 32 32" aria-hidden="true"><circle cx="16" cy="16" r="15" fill="#fff"/><rect x="11" y="7" width="10" height="18" rx="2" fill="none" stroke="var(--green-b)" stroke-width="2"/><rect x="13" y="10" width="6" height="6" fill="var(--green-b)"/></svg>
      0274829315
    </li>
    <li class="contact__item">
      <svg class="contact__icon" viewBox="0 0 32 32" aria-hidden="true"><circle cx="16" cy="16" r="15" fill="#fff"/><rect x="8" y="10" width="16" height="12" rx="1" fill="var(--green-b)"/><path d="M8 10 L16 17 L24 10" fill="none" stroke="#fff" stroke-width="1.5"/></svg>
      brightnode47@mailvista.example
    </li>
    <li class="contact__item">
      <svg class="contact__icon" viewBox="0 0 32 32" aria-hidden="true"><circle cx="16" cy="16" r="15" fill="#fff"/><path d="M16 25 C11 19 10 16 10 14 A6 6 0 0 1 22 14 C22 16 21 19 16 25 Z" fill="var(--green-b)"/><circle cx="16" cy="14" r="2.2" fill="#fff"/></svg>
      14c tamworth cl,kelvale
    </li>
  </ul>
</section>

</body>
</html>
```